Morrow Drift (Gems and Stones Online Personal Well Morrow Drift Experience)

Website design for a customer looking to start an online "experience" surrounding the sale of curated and personalized gem and stone sets built for personal health and well Morrow Drift. Customers will seek out the site to look for stones/gems that they can put in their pocket or carry with them and reference to gain power, enlightment, inspiration, etc. A change in the way they are thinking driven by a therapists background of knowledge in personal health.

Color codes, logos, notes and other website resources are attached in the uploaded document.

```html
<!DOCTYPE html>
<html lang="en">
<head>
<meta charset="utf-8">
<title>Morrow Drift — Gems and Stones for Well Being</title>
<link href="https://fonts.googleapis.com/css2?family=Mulish:wght@300;400;500;600;700&display=swap" rel="stylesheet">
<style>
:root{
  --ink:#111111;
  --text:#6b6b6b;
  --sand:#d9cfc5;
  --peach:#f3dcc6;
  --band:#f6e3d0;
  --accent:#d9a074;
  --white:#ffffff;
  --line:#e6e6e6;
}
*{box-sizing:border-box;margin:0;padding:0}
html,body{width:1200px;height:4580px;overflow:hidden;background:var(--white)}
body{position:relative;font-family:'Mulish',sans-serif;color:var(--ink)}
.abs{position:absolute}
.deco-ring{position:absolute;border:5px solid var(--peach);border-radius:50%}
/* header */
.top-tab{left:347px;top:0;width:506px;height:30px;background:var(--sand);border-radius:0 0 50% 50%/0 0 100% 100%}
.handle{left:0;width:1200px;top:7px;text-align:center;font-size:14px;color:#333}
.handle i{display:inline-block;width:13px;height:13px;border:2px solid #222;border-radius:50%;vertical-align:-2px;margin-right:6px}
.brand{left:153px;top:32px;width:124px;height:124px;border-radius:50%;background:var(--white);border:2px solid var(--sand);display:flex;align-items:center;justify-content:center;text-align:center;font-size:19px;font-weight:300;color:#bfb3a6;line-height:1.1;z-index:3}
.nav{left:344px;top:52px;display:flex;gap:32px;font-size:13px;color:#222;letter-spacing:.2px}
.cart{left:1030px;top:46px}
/* hero */
.hero{left:0;top:101px;width:1200px;height:500px;background:radial-gradient(circle at 28% 30%,#3ba9b8 0,#2a6f80 18%,transparent 36%),radial-gradient(circle at 60% 12%,#c59bb8 0,transparent 16%),linear-gradient(135deg,#3a3430,#4b3a2e 50%,#2c2622)}
.hero-curve{left:0;top:101px}
.welcome{left:765px;top:196px;width:284px;height:284px;border-radius:50%;border:4px solid var(--sand);display:flex;flex-direction:column;align-items:center;justify-content:center;color:var(--white);text-align:center}
.welcome small{font-size:18px;font-weight:300}
.welcome h1{font-size:44px;font-weight:400;line-height:1.2}
.welcome .down{margin-top:10px;width:22px;height:22px;border:2px solid #fff;border-radius:50%;font-size:12px;line-height:18px}
.dots{left:1131px;top:322px;display:flex;flex-direction:column;gap:8px}
.dots span{width:6px;height:6px;border-radius:50%;background:#fff}
/* subscription */
.subscribe{left:226px;top:595px;width:748px;height:178px;background:var(--sand);box-shadow:0 18px 20px -14px rgba(0,0,0,.25)}
.subscribe h2{position:absolute;top:30px;width:100%;text-align:center;font-size:40px;font-weight:400}
.field{position:absolute;background:var(--white);font-size:12px;color:#444;padding:0 22px;display:flex;align-items:center}
.btn{position:absolute;background:var(--ink);color:var(--white);font-size:12px;font-weight:600;display:flex;align-items:center;justify-content:center;letter-spacing:.2px}
/* sections */
.section-title{left:0;width:1200px;text-align:center;font-size:38px;font-weight:400}
.card{position:absolute;width:293px;height:329px;border:3px solid var(--ink);background:var(--white)}
.card .ph{position:absolute;left:10px;top:10px;width:267px;height:228px}
.card .name{position:absolute;left:24px;top:256px;font-size:15px}
.card .price{position:absolute;left:24px;top:285px;font-size:16px;color:var(--accent);font-weight:300}
.card .btn{left:180px;top:259px;width:106px;height:32px;font-size:11px}
.arrow{position:absolute}
/* curated */
.curated-photo{left:601px;top:1815px;width:599px;height:507px;background:radial-gradient(circle at 50% 60%,#48a6a0 0,transparent 22%),linear-gradient(135deg,#7a5a3a,#3d2c1e 60%,#2a1f16)}
.curated-card{left:144px;top:1867px;width:530px;height:403px;background:var(--white);box-shadow:0 0 12px rgba(0,0,0,.06);padding:60px 70px}
.curated-card h2,.about h2,.consult h2{font-size:40px;font-weight:400}
.body-copy{font-size:13px;line-height:24px;color:var(--text);text-align:justify}
.play{left:861px;top:2028px;width:80px;height:80px;border-radius:50%;background:#4a4a4a;border:5px solid #e8e8e8}
/* circles */
.circle-photo{position:absolute;width:434px;height:434px;border-radius:50%;border:6px solid var(--peach);padding:10px;background:var(--white)}
.circle-photo div{width:100%;height:100%;border-radius:50%}
.divider{left:144px;top:3378px;width:1030px;height:1px;background:var(--line)}
/* blog */
.post{position:absolute;width:439px;height:153px;border:2px solid var(--line);background:var(--white)}
.post .ph{position:absolute;left:6px;top:6px;width:157px;height:140px}
.post h3{position:absolute;left:186px;top:14px;font-size:17px;font-weight:400}
.post p{position:absolute;left:186px;top:44px;width:238px;font-size:11px;line-height:18px;color:var(--text)}
.post .meta{position:absolute;left:186px;top:118px;font-size:10px;display:flex;align-items:center;gap:10px;color:#333}
.post .meta i{width:26px;height:26px;border-radius:50%;background:#b9a89a}
.post .meta b{font-weight:400;color:var(--accent);text-decoration:underline;margin-left:12px}
/* testimonials */
.testimonials{left:0;top:3764px;width:1200px;height:405px;background:var(--band)}
.stars{left:304px;top:3943px;font-size:22px;letter-spacing:3px}
.quote{left:304px;top:3986px;width:720px;font-size:14px;font-style:italic;line-height:24px;color:#333}
.signed{left:304px;top:4066px;font-size:16px;font-style:italic}
/* footer */
.foot-title{font-size:24px;font-weight:400;top:4224px}
.foot-links{top:4277px;font-size:13px;line-height:25.6px;color:#555;list-style:none}
.socials{left:160px;top:4503px;display:flex;gap:8px}
.socials span{width:24px;height:24px;border:1.5px solid #555;border-radius:50%}
.copyright{left:560px;top:4506px;width:484px;text-align:right;font-size:12px;color:#444}
.footer-field{border:1.5px solid #999;font-size:11px;padding:0 14px}
</style>
</head>
<body>

<div class="deco-ring" style="left:-380px;top:525px;width:480px;height:480px"></div>
<div class="deco-ring" style="left:1105px;top:1030px;width:480px;height:480px"></div>
<div class="deco-ring" style="left:-310px;top:1830px;width:470px;height:470px"></div>
<div class="deco-ring" style="left:1080px;top:3560px;width:380px;height:380px"></div>
<div class="deco-ring" style="left:-290px;top:4270px;width:420px;height:420px"></div>

<!-- header -->
<div class="abs top-tab"></div>
<div class="abs handle"><i></i>@morrow.drift</div>
<div class="abs brand">Morrow<br>Drift</div>
<nav class="abs nav">
  <span>SUBSCRIPTIONS</span><span>COLLECTIONS</span><span>ACCESSORIES</span><span>CUSTOM CURATED SETS</span><span>ABOUT US</span>
</nav>
<svg class="abs cart" width="26" height="24" viewBox="0 0 26 24" fill="none" stroke="#111" stroke-width="2"><path d="M1 3h4l3 12h13l3-9H7"/><circle cx="10" cy="20" r="1.8" fill="#111"/><circle cx="19" cy="20" r="1.8" fill="#111"/></svg>

<!-- hero -->
<div class="abs hero" role="img" aria-label="Turquoise, pink and blue raw crystals with gold nuggets scattered on dark wood"></div>
<svg class="abs hero-curve" width="1200" height="500" viewBox="0 0 1200 500"><path d="M0 369 Q600 619 1200 369 L1200 500 L0 500 Z" fill="#fff"/></svg>
<div class="abs welcome">
  <small>Welcome to</small>
  <h1>Morrow<br>Drift</h1>
  <div class="down">↓</div>
</div>
<div class="abs dots"><span></span><span></span><span></span></div>

<!-- subscription -->
<section class="abs subscribe">
  <h2>Monthly Subscription</h2>
  <div class="field" style="left:44px;top:100px;width:251px;height:43px">Enter Name</div>
  <div class="field" style="left:304px;top:100px;width:250px;height:43px">Enter Email</div>
  <div class="btn" style="left:563px;top:100px;width:139px;height:43px;font-size:16px;font-weight:500">SUBSCRIBE</div>
</section>

<!-- collections -->
<h2 class="abs section-title" style="top:850px">Collections</h2>
<div class="card" style="left:144px;top:924px"><div class="ph" role="img" aria-label="Birthday cake with lit candles and balloons" style="background:linear-gradient(160deg,#3d6fb5,#c84a7a 50%,#e7d6c8)"></div><span class="name">BIRTHDAY</span><span class="price">$67.89</span><span class="btn">ADD TO CART</span></div>
<div class="card" style="left:453px;top:924px"><div class="ph" role="img" aria-label="Modern white house exterior" style="background:linear-gradient(180deg,#d9dde2,#8a8d8f 70%,#5e7a4e)"></div><span class="name">HOUSE WARMING</span><span class="price">$67.89</span><span class="btn">ADD TO CART</span></div>
<div class="card" style="left:763px;top:924px"><div class="ph" role="img" aria-label="Client in a counselling session" style="background:linear-gradient(120deg,#4a3226,#c98a3a 45%,#d8d2c9)"></div><span class="name">GRIEF</span><span class="price">$67.89</span><span class="btn">ADD TO CART</span></div>
<svg class="arrow" style="left:80px;top:1070px" width="22" height="40" viewBox="0 0 22 40" fill="none" stroke="#888" stroke-width="2"><path d="M20 2 2 20l18 18"/></svg>
<svg class="arrow" style="left:1098px;top:1070px" width="22" height="40" viewBox="0 0 22 40" fill="none" stroke="#888" stroke-width="2"><path d="M2 2l18 18L2 38"/></svg>

<!-- accessories -->
<h2 class="abs section-title" style="top:1330px">Accessories</h2>
<div class="card" style="left:144px;top:1404px"><div class="ph" role="img" aria-label="Brass singing bowl with mallet" style="background:linear-gradient(150deg,#2b2520,#7a5a34 55%,#3a2e24)"></div><span class="name">BOWLS</span><span class="price">$67.89</span><span class="btn">ADD TO CART</span></div>
<div class="card" style="left:453px;top:1404px"><div class="ph" role="img" aria-label="Lit white candles" style="background:linear-gradient(160deg,#9fb0b5,#e9e3da 55%,#d8a46a)"></div><span class="name">CANDLES</span><span class="price">$67.89</span><span class="btn">ADD TO CART</span></div>
<div class="card" style="left:763px;top:1404px"><div class="ph" role="img" aria-label="Assorted polished gemstones" style="background:linear-gradient(135deg,#b85a5a,#4a6a6a 40%,#8a7aa8 70%,#e3d9d0)"></div><span class="name">STONES</span><span class="price">$67.89</span><span class="btn">ADD TO CART</span></div>
<svg class="arrow" style="left:80px;top:1550px" width="22" height="40" viewBox="0 0 22 40" fill="none" stroke="#888" stroke-width="2"><path d="M20 2 2 20l18 18"/></svg>
<svg class="arrow" style="left:1098px;top:1550px" width="22" height="40" viewBox="0 0 22 40" fill="none" stroke="#888" stroke-width="2"><path d="M2 2l18 18L2 38"/></svg>

<!-- custom curated sets -->
<div class="abs curated-photo" role="img" aria-label="Video still of blue and turquoise stones poured onto a wooden table"></div>
<div class="abs play"><svg width="70" height="70" viewBox="0 0 70 70"><path d="M26 20v30l24-15z" fill="#fff"/></svg></div>
<section class="abs curated-card">
  <h2>Custom Curated Sets</h2>
  <p class="body-copy" style="margin-top:14px">Sed ut perspiciatis unde omnis iste natus error sit voluptatem accusantium doloremque laudantium, totam rem aperiam, eaque ipsa quae ab illo inventore veritatis et quasi architecto beatae vitae dicta sunt explicabo enim ipsam voluptatem quia voluptas sit aspernatur aut odit aut fugit,</p>
  <span class="btn" style="left:71px;top:293px;width:150px;height:41px">VIEW PRODUCTS</span>
  <span class="btn" style="left:231px;top:293px;width:149px;height:41px">SUBSCRIBE NOW</span>
</section>

<!-- about -->
<div class="circle-photo" style="left:133px;top:2382px"><div role="img" aria-label="Smiling couple sitting together" style="background:linear-gradient(135deg,#d8d0c4,#8a6a52 45%,#3a3a3c)"></div></div>
<section class="abs about" style="left:594px;top:2415px;width:468px">
  <h2>About Us</h2>
  <p class="body-copy" style="margin-top:14px">Sed ut perspiciatis unde omnis iste natus error sit voluptatem accusantium doloremque laudantium, totam rem aperiam, eaque ipsa quae ab illo inventore veritatis et quasi architecto beatae vitae dicta sunt explicabo enim ipsam voluptatem quia voluptas sit aspernatur aut odit aut fugit, Sed ut perspiciatis unde omnis iste natus error sit voluptatem accusantium doloremque laudantium, totam rem aperiam, eaque ipsa quae ab illo inventore veritatis et quasi architecto beatae vitae dicta sunt explicabo enim ipsam voluptatem quia voluptas sit aspernatur aut odit aut fugit,</p>
  <span class="btn" style="left:0;top:311px;width:126px;height:42px">READ MORE</span>
</section>

<!-- consultations -->
<section class="abs consult" style="left:148px;top:2905px;width:432px">
  <h2>Consultations</h2>
  <p class="body-copy" style="margin-top:14px">Sed ut perspiciatis unde omnis iste natus error sit voluptatem accusantium doloremque laudantium, totam rem aperiam, eaque ipsa quae ab illo inventore veritatis et quasi architecto beatae vitae dicta sunt explicabo enim ipsam voluptatem quia voluptas sit aspernatur aut odit aut fugit, Sed ut perspiciatis unde omnis iste natus error sit voluptatem accusantium doloremque laudantium, totam rem aperiam, eaque ipsa quae ab illo inventore veritatis et quasi architecto beatae vitae dicta sunt explicabo enim ipsam voluptatem quia voluptas</p>
  <span class="btn" style="left:0;top:309px;width:127px;height:42px">READ MORE</span>
</section>
<div class="circle-photo" style="left:624px;top:2868px"><div role="img" aria-label="Therapist seated with a notepad during a consultation" style="background:linear-gradient(135deg,#c9c2b4,#8a7a5a 45%,#5a5a4a)"></div></div>

<div class="abs divider"></div>

<!-- blog -->
<h2 class="abs section-title" style="top:3445px">Wellness Blog</h2>
<article class="post" style="left:153px;top:3531px">
  <div class="ph" role="img" aria-label="Dark tray with a white flower" style="background:linear-gradient(135deg,#1e2a36,#5a6a78 50%,#1a1a1a)"></div>
  <h3>Sed quia non numquam eius</h3>
  <p>Ut enim ad minima veniam, quis nostrum exercitationem ullam corporis suscipit laboriosam, nisi ut aliquid</p>
  <div class="meta"><i></i>James &nbsp;|&nbsp; May 14,2021<b>READ MORE</b></div>
</article>
<article class="post" style="left:608px;top:3531px">
  <div class="ph" role="img" aria-label="Glowing candle with festive lights" style="background:radial-gradient(circle at 50% 60%,#e08a3a,#6a3a1e 45%,#2a2a1a)"></div>
  <h3>Sed quia non numquam eius</h3>
  <p>Ut enim ad minima veniam, quis nostrum exercitationem ullam corporis suscipit laboriosam, nisi ut aliquid</p>
  <div class="meta"><i></i>James &nbsp;|&nbsp; May 14,2021<b>READ MORE</b></div>
</article>
<svg class="arrow" style="left:80px;top:3589px" width="22" height="40" viewBox="0 0 22 40" fill="none" stroke="#888" stroke-width="2"><path d="M20 2 2 20l18 18"/></svg>
<svg class="arrow" style="left:1098px;top:3589px" width="22" height="40" viewBox="0 0 22 40" fill="none" stroke="#888" stroke-width="2"><path d="M2 2l18 18L2 38"/></svg>

<!-- testimonials -->
<section class="abs testimonials"></section>
<h2 class="abs section-title" style="top:3840px">Customer Testimonials</h2>
<div class="abs" role="img" aria-label="Customer portrait" style="left:171px;top:3947px;width:106px;height:106px;border-radius:50%;background:linear-gradient(135deg,#e8e4de,#a88a72)"></div>
<div class="abs stars">★★★★★</div>
<p class="abs quote">"Sed ut perspiciatis unde omnis iste natus error sit voluptatem accusantium doloremque laudantium, totam rem aperiam, eaque ipsa quae ab illo inventore veritatis et quasi architecto beatae vitae dicta sed quia consequuntur magni dolores eos qui ratione voluptatem sequi nesciunt"</p>
<p class="abs signed">-JOHN DOE</p>
<svg class="arrow" style="left:80px;top:3987px" width="22" height="40" viewBox="0 0 22 40" fill="none" stroke="#888" stroke-width="2"><path d="M20 2 2 20l18 18"/></svg>
<svg class="arrow" style="left:1098px;top:3987px" width="22" height="40" viewBox="0 0 22 40" fill="none" stroke="#888" stroke-width="2"><path d="M2 2l18 18L2 38"/></svg>

<!-- footer -->
<h3 class="abs foot-title" style="left:155px">Menus</h3>
<ul class="abs foot-links" style="left:157px"><li>Subscriptions</li><li>Collections</li><li>Accessories</li><li>Custom Curated Sets</li><li>About Us</li></ul>
<h3 class="abs foot-title" style="left:437px">Other Links</h3>
<ul class="abs foot-links" style="left:440px"><li>My Account</li><li>Cart</li><li>Checkout</li><li>Thank You</li><li>Terms and Conditions</li><li>Privacy Policy</li></ul>
<h3 class="abs foot-title" style="left:699px">Contact us</h3>
<div class="field footer-field" style="left:699px;top:4274px;width:167px;height:39px">Enter Name</div>
<div class="field footer-field" style="left:875px;top:4274px;width:169px;height:39px">Enter Name</div>
<div class="field footer-field" style="left:699px;top:4324px;width:345px;height:62px;align-items:flex-start;padding-top:12px">Message</div>
<span class="btn" style="left:699px;top:4395px;width:73px;height:30px;font-size:11px">SUBMIT</span>
<div class="abs socials"><span></span><span></span><span></span><span></span><span></span></div>
<p class="abs copyright">© 2024 morrowdrift. All rights reserved.Privacy &nbsp;|&nbsp; Terms of Use</p>

</body>
</html>
```